Vornfield Business Cards

Logo files are included. Full "Vornfield" logo should be included on the back of the business card. The H symbol should be included on the front with the contact information.

Vornfield, LLC is the company name and we do commercial construction and real estate development consulting services. Look for a fairly simple card design utilizing our logo.

```html
<!DOCTYPE html>
<html lang="en">
<head>
<meta charset="utf-8">
<title>Vornfield Business Cards</title>
<link href="https://fonts.googleapis.com/css2?family=Montserrat:wght@500&family=Poppins:wght@400;600;700;800&display=swap" rel="stylesheet">
<style>
  :root {
    --navy: #1a3a4e;
    --gold: #ebae00;
    --paper: #f1f1f1;
    --white: #ffffff;
    --page: #ffffff;
  }
  * { margin: 0; padding: 0; box-sizing: border-box; }
  html, body {
    width: 1051px; height: 1200px; overflow: hidden;
    background: var(--page);
    font-family: "Poppins", sans-serif;
  }
  .canvas { position: relative; width: 1051px; height: 1200px; }

  .card {
    position: absolute; left: 106px; width: 840px; height: 480px;
    border-radius: 30px; overflow: hidden;
    box-shadow: 0 6px 14px rgba(0,0,0,0.12);
  }
  .card--back { top: 81px; background: var(--paper); }
  .card--front { top: 639px; background: var(--gold); }

  /* Back: brand block */
  .brand-mark {
    position: absolute; left: 354px; top: 120px;
    width: 132px; height: 132px; border-radius: 50%;
    border: 7px solid var(--navy);
  }
  .brand-name {
    position: absolute; left: 0; right: 0; top: 262px;
    text-align: center;
    font-family: "Montserrat", sans-serif; font-weight: 500;
    font-size: 66px; letter-spacing: 1px; line-height: 1;
    color: var(--navy);
  }

  /* Front: identity */
  .badge {
    position: absolute; left: 46px; top: 174px;
    width: 134px; height: 134px; border-radius: 50%;
    background: var(--white);
    display: flex; align-items: center; justify-content: center;
    font-weight: 600; font-size: 21px; color: var(--navy);
  }
  .name-rule {
    position: absolute; left: 197px; top: 204px;
    width: 9px; height: 65px; background: var(--navy);
  }
  .person-name {
    position: absolute; left: 226px; top: 192px;
    font-weight: 800; font-size: 49px; line-height: 1;
    letter-spacing: -1px; color: var(--navy);
  }
  .person-role {
    position: absolute; left: 226px; top: 248px;
    font-weight: 400; font-size: 29px; line-height: 1;
    letter-spacing: 1px; color: var(--navy);
  }

  .divider {
    position: absolute; left: 488px; top: 72px;
    width: 2px; height: 334px; background: var(--white);
  }

  .contact {
    position: absolute; left: 515px; height: 46px;
    display: flex; align-items: center;
  }
  .contact__icon {
    width: 46px; height: 46px; border-radius: 50%;
    background: var(--white); flex: none;
    display: flex; align-items: center; justify-content: center;
  }
  .contact__text { margin-left: 8px; color: var(--white); }
  .contact__label { font-size: 17px; font-weight: 400; line-height: 1.1; }
  .contact__value { font-size: 19px; font-weight: 700; letter-spacing: 2px; line-height: 1.1; }

  .contact--address { top: 72px; }
  .contact--web { top: 168px; }
  .contact--mail { top: 263px; }
  .contact--phone { top: 360px; }
</style>
</head>
<body>
<div class="canvas">

  <section class="card card--back">
    <div class="brand-mark"></div>
    <div class="brand-name">VORNFIELD</div>
  </section>

  <section class="card card--front">
    <div class="badge">Vornfield</div>
    <div class="name-rule"></div>
    <div class="person-name">John Doe</div>
    <div class="person-role">Designation</div>

    <div class="divider"></div>

    <div class="contact contact--address">
      <div class="contact__icon">
        <svg width="20" height="26" viewBox="0 0 20 26"><path d="M10 1a8 8 0 0 0-8 8c0 6 8 15 8 15s8-9 8-15a8 8 0 0 0-8-8z" fill="var(--navy)"/><circle cx="10" cy="9" r="4" fill="var(--white)"/></svg>
      </div>
      <div class="contact__text">
        <div class="contact__label">Visit Us here</div>
        <div class="contact__value">Your Address</div>
      </div>
    </div>

    <div class="contact contact--web">
      <div class="contact__icon">
        <svg width="34" height="34" viewBox="0 0 34 34" fill="none" stroke="var(--navy)" stroke-width="1.3"><circle cx="17" cy="17" r="15"/><ellipse cx="17" cy="17" rx="7" ry="15"/><line x1="17" y1="2" x2="17" y2="32"/><line x1="2" y1="17" x2="32" y2="17"/><path d="M5 9h24M5 25h24"/></svg>
      </div>
      <div class="contact__text">
        <div class="contact__label">Visit Our Website</div>
        <div class="contact__value">www.company.com</div>
      </div>
    </div>

    <div class="contact contact--mail">
      <div class="contact__icon">
        <svg width="28" height="20" viewBox="0 0 28 20" fill="none" stroke="var(--navy)" stroke-width="1.6"><rect x="1" y="1" width="26" height="18" rx="3"/><path d="M2 3l12 9 12-9"/></svg>
      </div>
      <div class="contact__text">
        <div class="contact__label">Get Your Support</div>
        <div class="contact__value">mail@company.com</div>
      </div>
    </div>

    <div class="contact contact--phone">
      <div class="contact__icon">
        <svg width="24" height="24" viewBox="0 0 24 24"><path d="M6.6 2.5l3 3.2-2 2.6c1.3 2.8 3.4 4.9 6.2 6.2l2.6-2 3.2 3-1.8 3.3C11 19 5 13 2.8 4.3z" fill="var(--navy)"/></svg>
      </div>
      <div class="contact__text">
        <div class="contact__label">For more information</div>
        <div class="contact__value">+880-1223XXXX</div>
      </div>
    </div>
  </section>

</div>
</body>
</html>
```